The Quiet Hour Safeguard Handbook

A book cover. The book will be marketed as a promotional item for financial advisors, financial planners, independent insurance agents, bankers, and any professional who views their role as guardian of their clients assets and helping them manage risk.

```html
<!DOCTYPE html>
<html lang="en">
<head>
<meta charset="UTF-8">
<title>The Quiet Hour Safeguard Handbook – Cover</title>
<link rel="stylesheet" href="https://fonts.googleapis.com/css2?family=Inter:ital,wght@0,400;0,500;0,700;1,600&display=swap">
<style>
  :root {
    --navy: #16284d;
    --navy-deep: #0f1d3a;
    --gold: #e0ad3a;
    --gold-soft: #c9963a;
    --white: #ffffff;
    --sky-top: #1e3560;
    --sky-mid: #5a6f8e;
    --glow: #f2b25a;
    --ridge: #2a2f33;
    --ground: #1a1a1c;
  }
  * { margin: 0; padding: 0; box-sizing: border-box; }
  html, body { width: 800px; height: 1200px; overflow: hidden; background: var(--navy); }
  .cover {
    position: relative; width: 800px; height: 1200px;
    background: var(--navy);
    font-family: "Inter", sans-serif; color: var(--white);
    overflow: hidden;
  }
  .divider { position: absolute; left: 0; width: 100%; display: flex; justify-content: center; z-index: 3; }
  .divider svg { display: block; }
  .divider--top { top: 44px; }
  .divider--mid { top: 416px; }
  .title {
    position: absolute; top: 82px; left: 40px; right: 40px; z-index: 3;
    text-align: center; font-weight: 700; font-size: 60px; line-height: 1.15;
    letter-spacing: -0.5px;
  }
  .subtitle {
    position: absolute; top: 304px; left: 40px; right: 40px; z-index: 3;
    text-align: center; font-style: italic; font-weight: 600;
    font-size: 26px; line-height: 1.4; color: var(--gold);
  }
  .scene {
    position: absolute; top: 396px; left: 0; width: 800px; height: 516px; z-index: 1;
    background:
      linear-gradient(180deg, rgba(22,40,77,1) 0%, rgba(22,40,77,0) 18%),
      radial-gradient(ellipse 55% 22% at 62% 60%, rgba(255,210,130,0.95) 0%, rgba(242,178,90,0.6) 35%, rgba(242,178,90,0) 100%),
      linear-gradient(180deg, var(--sky-top) 0%, var(--sky-mid) 40%, #c89a6a 58%, var(--ridge) 70%, var(--ground) 100%);
  }
  .emblem { position: absolute; top: 452px; left: 50%; transform: translateX(-50%); z-index: 3; }
  .feature-band {
    position: absolute; top: 912px; left: 0; width: 800px; height: 288px;
    background: var(--navy); border-top: 1px solid rgba(224,173,58,0.5);
  }
  .features {
    position: absolute; top: 28px; left: 50px; right: 50px;
    display: flex; justify-content: space-between; list-style: none;
  }
  .feature {
    flex: 1; display: flex; flex-direction: column; align-items: center; gap: 12px;
    border-left: 1px solid var(--gold-soft);
  }
  .feature:first-child { border-left: none; }
  .feature svg { width: 42px; height: 42px; }
  .feature__label { font-size: 14px; font-weight: 500; letter-spacing: 0.3px; text-transform: uppercase; }
  .tagline {
    position: absolute; top: 170px; left: 40px; right: 40px;
    text-align: center; text-transform: uppercase; font-weight: 400;
    font-size: 21px; line-height: 1.45; letter-spacing: 1.5px;
  }
</style>
</head>
<body>
<main class="cover">
  <div class="divider divider--top">
    <svg width="340" height="16" viewBox="0 0 340 16"><line x1="0" y1="8" x2="150" y2="8" stroke="#e0ad3a" stroke-width="1.5"/><rect x="164" y="2" width="12" height="12" transform="rotate(45 170 8)" fill="#e0ad3a"/><line x1="190" y1="8" x2="340" y2="8" stroke="#e0ad3a" stroke-width="1.5"/></svg>
  </div>

  <h1 class="title">The Quiet Hour<br>Safeguard<br>Handbook</h1>
  <p class="subtitle">Protect Yourself and Your Family<br>in the AI Age</p>

  <div class="scene" role="img" aria-label="Photograph of a family of four holding hands on a hilltop, seen from behind, looking over mountains and a lake at sunrise"></div>

  <div class="divider divider--mid">
    <svg width="340" height="16" viewBox="0 0 340 16"><line x1="0" y1="8" x2="150" y2="8" stroke="#e0ad3a" stroke-width="1.5"/><rect x="164" y="2" width="12" height="12" transform="rotate(45 170 8)" fill="#e0ad3a"/><line x1="190" y1="8" x2="340" y2="8" stroke="#e0ad3a" stroke-width="1.5"/></svg>
  </div>

  <svg class="emblem" width="170" height="190" viewBox="0 0 170 190" aria-hidden="true">
    <path d="M85 6 C120 22 148 24 164 24 C164 110 140 158 85 184 C30 158 6 110 6 24 C22 24 50 22 85 6 Z" fill="#16284d" stroke="#e0ad3a" stroke-width="7"/>
    <path d="M85 22 C114 34 136 37 150 37 C149 108 128 148 85 170 C42 148 21 108 20 37 C34 37 56 34 85 22 Z" fill="none" stroke="#e0ad3a" stroke-width="1.5" opacity="0.7"/>
  </svg>

  <section class="feature-band">
    <ul class="features">
      <li class="feature">
        <svg viewBox="0 0 42 42"><path d="M21 3 L36 9 V20 C36 30 29 36 21 39 C13 36 6 30 6 20 V9 Z" fill="none" stroke="#e0ad3a" stroke-width="2.5"/><circle cx="21" cy="17" r="4.5" fill="#e0ad3a"/><path d="M13 31 C14 25 28 25 29 31 Z" fill="#e0ad3a"/></svg>
        <span class="feature__label">Protect</span>
      </li>
      <li class="feature">
        <svg viewBox="0 0 42 42"><path d="M13 19 V13 a8 8 0 0 1 16 0 V19" fill="none" stroke="#e0ad3a" stroke-width="3"/><rect x="9" y="19" width="24" height="19" rx="2" fill="#e0ad3a"/><circle cx="21" cy="28" r="2.5" fill="#16284d"/></svg>
        <span class="feature__label">Secure</span>
      </li>
      <li class="feature">
        <svg viewBox="0 0 42 42"><circle cx="21" cy="12" r="5" fill="#e0ad3a"/><circle cx="10" cy="16" r="4" fill="#e0ad3a"/><circle cx="32" cy="16" r="4" fill="#e0ad3a"/><path d="M12 32 C12 21 30 21 30 32 Z" fill="#e0ad3a"/><path d="M2 32 C2 24 14 23 14 28 L13 32 Z" fill="#e0ad3a"/><path d="M40 32 C40 24 28 23 28 28 L29 32 Z" fill="#e0ad3a"/></svg>
        <span class="feature__label">Empower</span>
      </li>
      <li class="feature">
        <svg viewBox="0 0 42 42" fill="none" stroke="#e0ad3a" stroke-width="2"><ellipse cx="21" cy="21" rx="4" ry="6"/><ellipse cx="21" cy="21" rx="9" ry="12"/><ellipse cx="21" cy="21" rx="14" ry="18"/></svg>
        <span class="feature__label">Prepare</span>
      </li>
      <li class="feature">
        <svg viewBox="0 0 42 42"><circle cx="21" cy="21" r="17" fill="none" stroke="#e0ad3a" stroke-width="2.5"/><path d="M13 21 L19 27 L31 14" fill="none" stroke="#e0ad3a" stroke-width="3.5" stroke-linecap="round" stroke-linejoin="round"/></svg>
        <span class="feature__label">Peace of Mind</span>
      </li>
    </ul>
    <p class="tagline">It’s better to have it<br>and not need it than need it<br>and not have it.</p>
  </section>
</main>
</body>
</html>
```